Tessaro Lane Website

We are starting a marketing company and to do that we need a website! We want a website that will inspire and persuade to bring out the awesomeness in our clients.
What we want to see:
- Inspirational and persuasive imagery that relate to Branding.
- No cliche images eg. business man, suits and hand shakes
- We want to transform and educate our clients.
- We want to show them the path and would like our website to really act as a guide that guides them step by step through our process.
- We want the portray that we are an investment but not have a pretentious way to it. We put our heart into every project and that is how we treat our clients.
-When you submit your design please include what platform you have created for. Preference would be Wordpress or Joobla.

We have included the psd file for the wire frame, logo files, font files, site map and a link to a video we create to give you more information on what we would like to see. http://clipvault-demo.example/t/qx903LmaP

Feel free to make small modification to the logos if you think it will improve it. Your creativity and advice is most welcome.

One thing we forgot. We would like to have our contact information near the top of the website as well as at the bottom.  Here is out contact info:

Email: info@tessarolane.ca
Phone: 555-013-4829

Reason: As we are new with the platform and that we want to optimize our results, we decided to extend the deadline by 15 days. Thanks!

Target Market(s)

28-60, Male and Female, Oil field, Local Businesses, Dentists, Chiropractors, Hair salon, Construction/Renovation, Events etc

Industry/Entity Type

Investment

Requirements
Must have
• - 4 Inspirational and persuasive Imagery for the top portion of the website
- Must have a feel as if your not on a website an example of this is linked below.
http://www.pitchgallery-demo.example/design/482907/web-design-by-dalia-fenwick
Nice to have
• - Creative advice from you.
- Creative buttons for Get Free Quote and Subscribe buttons. Something out of the box that draws peoples attention. eg. a 'B' button. Just and example but still something related to branding.
Should not have
• No Cliches

```html
<!DOCTYPE html>
<html lang="en">
<head>
<meta charset="utf-8">
<title>Tessaro Lane</title>
<link rel="stylesheet" href="https://fonts.googleapis.com/css2?family=Fredoka:wght@500;600&family=Arimo:wght@400;700&display=swap">
<style>
:root{
  --green:#7f9f2a;
  --green-dark:#5f7d1e;
  --green-bar:#8aaa3e;
  --ink:#3a3a3a;
  --text:#5c5c5c;
  --page:#efefef;
  --header-top:#e4e4e4;
  --header-bottom:#c9c9c9;
  --footer:#1d1d1d;
  --muted:#8a8a8a;
  --line:#f4f4f4;
  --line-dark:#c4c4c4;
}
*{box-sizing:border-box;margin:0;padding:0}
html,body{width:1200px;height:718px;overflow:hidden}
body{background:var(--page);font-family:"Arimo",Arial,sans-serif;color:var(--text);position:relative}
.top-bar{position:absolute;left:0;top:0;width:1200px;height:9px;background:var(--green-bar)}
.header{position:absolute;left:0;top:9px;width:1200px;height:350px;background:linear-gradient(var(--header-top),var(--header-bottom))}
.brand{position:absolute;left:160px;top:24px;width:205px}
.brand-name{display:flex;align-items:center;gap:8px;font-family:"Fredoka",sans-serif;font-weight:600;font-size:30px;color:#7a7a7a;line-height:1}
.brand-dot{width:14px;height:14px;border-radius:50%;background:var(--green)}
.tagline{margin-top:16px;font-family:"Arimo",sans-serif;font-style:italic;font-weight:700;font-size:13px;color:#6d6d6d;padding-left:28px}
.main-nav{position:absolute;left:150px;top:120px;width:225px;list-style:none}
.main-nav li{height:37.7px;border-top:1px solid var(--line);border-bottom:1px solid var(--line-dark);display:flex;align-items:center;padding-left:20px;font-size:12.5px;font-weight:700;color:#444;letter-spacing:.3px}
.main-nav li::before{content:"";width:0;height:0;border-left:3px solid #9a9a9a;border-top:3px solid transparent;border-bottom:3px solid transparent;margin-right:20px}
.hero{position:absolute;left:375px;top:9px;width:675px;height:300px;background:radial-gradient(circle at 68% 30%,#f6fbe8 0,#d9efb4 18%,#b9e07a 38%,#9cc94c 62%,#c7e58a 100%)}
.hero-line{position:absolute;left:28px;top:149px;font-family:"Fredoka",sans-serif;font-weight:600;font-size:23px;color:var(--ink);letter-spacing:.2px;white-space:nowrap}
.hero-line .accent{color:var(--green)}
.hero-line .sep{margin:0 10px}
.slider-dots{position:absolute;right:3px;bottom:4px;display:flex;gap:3px}
.slider-dots span{width:15px;height:15px;background:#000;color:#fff;font-size:9px;font-weight:700;display:flex;align-items:center;justify-content:center}
.slider-dots span.active{background:var(--green)}
.connect{position:absolute;left:156px;top:317px;font-family:"Fredoka",sans-serif;font-weight:600;font-size:15px;line-height:15px;color:var(--green)}
.social{position:absolute;left:226px;top:320px;display:flex;gap:4px}
.social span{width:26px;height:26px;border-radius:50%;background:#a3a3a3}
.newsletter{position:absolute;left:391px;top:318px;font-family:"Fredoka",sans-serif;font-weight:600;font-size:21px;color:var(--ink);letter-spacing:.3px}
.btn{position:absolute;display:flex;align-items:center;justify-content:center;background:linear-gradient(#7d9f30,var(--green-dark));color:#fff;font-weight:700;font-size:15px;border-radius:2px;border:1px solid #5a7419}
.btn-subscribe{left:936px;top:316px;width:103px;height:34px}
.welcome{position:absolute;left:0;top:375px;width:1200px;text-align:center;font-family:"Fredoka",sans-serif;font-weight:600;font-size:22px;color:var(--green)}
.intro{position:absolute;left:300px;top:412px;width:600px;font-size:11.6px;line-height:17px;text-align:justify}
.intro p{margin-bottom:17px}
.intro .last{width:445px}
.btn-quote{left:769px;top:582px;width:131px;height:34px}
.footer{position:absolute;left:0;top:654px;width:1200px;height:64px;background:var(--footer);border-top:1px solid #333}
.footer-nav{position:absolute;top:12px;left:0;width:1200px;text-align:center;font-size:12.5px;color:var(--green)}
.footer-nav .pipe{margin:0 10px}
.copyright{position:absolute;top:38px;left:0;width:1200px;text-align:center;font-size:13px;color:var(--muted);letter-spacing:.3px}
</style>
</head>
<body>
<div class="top-bar"></div>
<header class="header">
  <div class="brand">
    <div class="brand-name"><span class="brand-dot"></span>Tessaro Lane</div>
    <div class="tagline">Because You´re Awesome!</div>
  </div>
</header>
<ul class="main-nav">
  <li>STRATEGY</li><li>PORTFOLIO</li><li>ABOUT US</li><li>CONTACT US</li><li>BLOG</li>
</ul>
<div class="hero" role="img" aria-label="Bright green leaves in sunlight with a translucent globe against a sky">
  <div class="hero-line"><span class="accent">TESSARO LANE</span><span class="sep">-</span>BE FOUND<span class="sep">-</span>CONNECT<span class="sep">-</span>GET GROWING</div>
  <div class="slider-dots"><span class="active">1</span><span>2</span><span>3</span><span>4</span></div>
</div>
<div class="connect">Connect<br>with us !</div>
<div class="social"><span></span><span></span><span></span><span></span><span></span></div>
<div class="newsletter">Get Tips and Tricks! Subscribe to our Newsletter.</div>
<div class="btn btn-subscribe">Subscribe</div>

<h1 class="welcome">WELCOME!</h1>
<div class="intro">
  <p>Lorem ipsum dolor sit amet, consectetur adipisicing elit, sed do eiusmod tempor incididunt ut labore et dolore magna aliqua. Ut enim ad minim veniam, quis nostrud exercitation ullamco laboris nisi ut aliquip ex ea commodo consequat. Duis aute irure dolor in reprehenderit in voluptate velit esse cillum dolore eu fugiat nulla pariatur. Excepteur sint occaecat cupidatat non proident, sunt in culpa qui officia deseruntilil</p>
  <p>Sed ut perspiciatis unde omnis iste natus error sit voluptatem accusantium doloremque laudantium, totam rem aperiam, eaque ipsa quae ab illo inventore veritatis et quasi architecto beatae vitae dicta sunt explicabo. Nemo enim ipsam voluptatem quia voluptas sit aspernatur aut odit aut fugit, sed quia consequuntur magni dolores eos qui ratione voluptatem sequi nesciunt. Neque porro quisquam est, qui dolom</p>
  <p class="last">aspernatur aut odit aut fugit, sed quia consequuntur magni dolores eos qui ratione voluptatem sequi nesciunt. Neque porro quisquam est, qui dolom</p>
</div>
<div class="btn btn-quote">Get a Free Quote</div>

<footer class="footer">
  <nav class="footer-nav">Site Map<span class="pipe">|</span>Strategy<span class="pipe">|</span>Portfolio<span class="pipe">|</span>About Us<span class="pipe">|</span>Contact Us<span class="pipe">|</span>Blog</nav>
  <div class="copyright">© TESSARO LANE INC. 2013</div>
</footer>
</body>
</html>
```